Classic Minimalistic Business Card

Design a classic, minimalistic Business Card. Please find inspiration in the attached Classic Minimalistic examples. My information:
Name: Glen Ovamir
Company: Ovamir Capital
Logo: OC
Address: 1470 N Thornwick Rd, Suite 210 | Geneva, IL 60134
Phone: 630-555-0192
Email: glenovamir@pvt.insure
Slogan: Building Strength Through Capital

Feel free to leave out any of the information above except my name.

I have selected Double-sided, but I am also open to Single-sided

Target Market(s)

22-70. income greater than 150k/year

Industry/Entity Type

Finance

Contact Information for Business Card

See Project Description

Requirements
Must have
• Ivory or "antiqued" background similar to the reference pictures

```html
<!DOCTYPE html>
<html lang="en">
<head>
<meta charset="utf-8">
<title>Ovamir Capital – Business Card</title>
<link rel="stylesheet" href="https://fonts.googleapis.com/css2?family=Cinzel:wght@600;700&family=Pinyon+Script&family=Exo+2:wght@400&display=swap">
<style>
  :root {
    --backdrop: #4a3a28;
    --card: #c9a881;
    --emboss: #b39168;
    --ink: #111111;
    --shadow: rgba(0, 0, 0, 0.45);
  }
  html, body {
    margin: 0;
    padding: 0;
    overflow: hidden;
  }
  .canvas {
    position: relative;
    width: 900px;
    height: 1200px;
    background: var(--backdrop);
    overflow: hidden;
  }
  .card {
    position: absolute;
    left: 80px;
    width: 742px;
    height: 441px;
    border-radius: 30px;
    background: var(--card);
    box-shadow: 0 4px 8px var(--shadow);
  }
  .card--front { top: 131px; }
  .card--back { top: 638px; }

  .monogram {
    position: absolute;
    left: 0;
    width: 100%;
    text-align: center;
    font-family: "Cinzel", serif;
    font-weight: 700;
    line-height: 1;
  }
  .card--front .monogram {
    top: 130px;
    font-size: 110px;
    color: var(--emboss);
  }
  .card--back .monogram {
    top: 50px;
    font-size: 84px;
    color: var(--ink);
  }

  .company {
    position: absolute;
    left: 0;
    width: 100%;
    text-align: center;
    font-family: "Cinzel", serif;
    font-weight: 700;
    line-height: 1;
    margin: 0;
  }
  .card--front .company {
    top: 312px;
    font-size: 40px;
    color: var(--emboss);
  }
  .card--back .company {
    top: 182px;
    font-size: 30px;
    color: var(--ink);
  }

  .person-name {
    position: absolute;
    top: 245px;
    left: 0;
    width: 100%;
    text-align: center;
    font-family: "Pinyon Script", cursive;
    font-size: 50px;
    line-height: 1;
    color: var(--ink);
    margin: 0;
  }

  .contact {
    position: absolute;
    top: 333px;
    left: 0;
    width: 100%;
    text-align: center;
    font-family: "Exo 2", sans-serif;
    font-size: 15px;
    line-height: 22px;
    letter-spacing: 0.6px;
    color: var(--ink);
    font-style: normal;
  }
  .contact span { display: block; }
</style>
</head>
<body>
  <main class="canvas">
    <section class="card card--front" aria-label="Card front">
      <div class="monogram">OC</div>
      <h2 class="company">OVAMIR CAPITAL</h2>
    </section>

    <section class="card card--back" aria-label="Card back">
      <div class="monogram">OC</div>
      <h2 class="company">OVAMIR CAPITAL</h2>
      <h1 class="person-name">Glen Ovamir</h1>
      <address class="contact">
        <span class="contact__phone">630-555-0192</span>
        <span class="contact__email">glenovamir@pvt.insure</span>
        <span class="contact__address">1470 N Thornwick Rd, Suite 210 | Geneva, IL 60134</span>
      </address>
    </section>
  </main>
</body>
</html>
```